Website and Mobile Devices design for food related application.

We need a design that is simple yet playful. The design should be food related if possible.
This design will be on the website and the mobile platform markets we intend application to be deployed too.
This application/website is called "Pickvoro[.com]. Its a random restaurant picker for the indecisive users.
Updates
Hi all, I picked a design. Again lots of great designs were submitted but I picked one that was more in line with what I wanted.
Target Market(s)
young internet savvy users.
Industry/Entity Type
Restaurant
Look and feel
Each slider illustrates characteristics of the customer's brand and the style your logo design should communicate.

```html
<!DOCTYPE html>
<html lang="en">
<head>
<meta charset="utf-8">
<title>Pickvoro</title>
<link href="https://fonts.googleapis.com/css2?family=Oswald:wght@300;400&display=swap" rel="stylesheet">
<style>
:root{
  --gold:#c0892a;
  --gold-text:#d4a257;
  --ink:#1b1a1f;
  --cream:#f8f3ea;
  --panel:#ece3d4;
  --card-text:#2e2a26;
  --loc:#8a6a35;
  --footer:#121212;
}
*{margin:0;padding:0;box-sizing:border-box}
html,body{width:1147px;height:1200px;overflow:hidden;background:var(--footer)}
.page{position:relative;width:1147px;height:1200px;font-family:Arial,Helvetica,sans-serif}
.hero{position:absolute;left:0;top:0;width:1147px;height:690px;
  background:linear-gradient(180deg,#3a2f2a 0%,#6b5240 25%,#b89a78 45%,#d9c2a0 60%,#3a2c24 100%)}
.nav-btn{position:absolute;top:56px;height:82px;background:var(--ink);border-radius:10px;padding:8px}
.nav-btn span{display:flex;align-items:center;justify-content:center;gap:8px;height:100%;background:var(--gold);border-radius:6px;
  color:#fff;font-family:'Oswald',sans-serif;font-weight:300;font-size:31px;letter-spacing:.5px}
.btn-refresh{left:152px;width:188px}
.btn-contact{left:793px;width:188px}
.link-bar{position:absolute;top:88px;height:16px;width:40px;background:var(--ink)}
.brand-frame{position:absolute;left:372px;top:33px;width:390px;height:140px;background:var(--ink);border-radius:14px;padding:10px}
.brand-inner{height:100%;border:5px solid var(--gold);border-radius:10px;background:var(--cream);
  display:flex;align-items:center;justify-content:center;
  font-family:'Oswald',sans-serif;font-weight:400;font-size:44px;color:var(--ink)}
.panel{position:absolute;left:8px;top:293px;width:1129px;height:766px;background:var(--panel);border-radius:12px}
.welcome{position:absolute;left:28px;top:22px;width:1067px;height:95px;background:var(--ink);border-radius:9px;text-align:center;
  font-family:'Oswald',sans-serif;font-weight:300}
.welcome h1{font-weight:300;font-size:31px;color:#fff;margin-top:10px;line-height:1.2}
.welcome p{font-size:19px;color:var(--gold-text);margin-top:4px}
.card{position:absolute;width:246px;height:232px;background:var(--cream);border-radius:9px;padding:10px 10px 0}
.card::after{content:"";position:absolute;left:8px;right:8px;bottom:-26px;height:22px;
  background:radial-gradient(ellipse at top,rgba(0,0,0,.28),rgba(0,0,0,0) 70%)}
.card .photo{width:228px;height:153px}
.card h2{font-family:'Oswald',sans-serif;font-weight:300;font-size:21px;color:var(--card-text);margin-top:6px;white-space:nowrap;line-height:1.2}
.card p{font-size:14px;color:var(--loc);margin-left:2px;white-space:nowrap}
.c1{left:27px}.c2{left:302px}.c3{left:578px}.c4{left:853px}
.r1{top:148px}.r2{top:452px}
.footer{position:absolute;left:0;top:1059px;width:1147px;height:141px}
.social{position:absolute;top:19px;left:471px;display:flex;gap:11px}
.social i{display:block;width:32px;height:32px;border-radius:50%;background:var(--gold)}
.rule{position:absolute;left:10px;right:10px;top:64px;border-top:1px dotted #6b5a3a}
.links{position:absolute;top:76px;width:100%;text-align:center;font-size:14px;color:var(--gold-text)}
.links a{color:var(--gold-text);text-decoration:none}
.copy{position:absolute;top:101px;width:100%;text-align:center;font-size:12px;color:#c8bfae}
</style>
</head>
<body>
<div class="page">
  <div class="hero" role="img" aria-label="Warmly lit lounge interior with round striped sofas"></div>

  <div class="link-bar" style="left:338px"></div>
  <div class="link-bar" style="left:758px"></div>
  <a class="nav-btn btn-refresh"><span>
    <svg width="36" height="36" viewBox="0 0 36 36" fill="none" stroke="#fff" stroke-width="4"><path d="M29 14a12 12 0 0 0-21-4"/><path d="M7 22a12 12 0 0 0 21 4"/><path d="M6 4v7h7" fill="#fff" stroke-width="2"/><path d="M30 32v-7h-7" fill="#fff" stroke-width="2"/></svg>
    REFRESH</span></a>
  <div class="brand-frame"><div class="brand-inner">Pickvoro</div></div>
  <a class="nav-btn btn-contact"><span>
    <svg width="38" height="38" viewBox="0 0 38 38" fill="none" stroke="#fff" stroke-width="3"><circle cx="19" cy="19" r="16"/><path d="M13 10l4 4-2 3c1 3 4 6 7 7l3-2 4 4-3 3c-7 0-16-9-16-16z" fill="#fff" stroke-width="1"/></svg>
    CONTACT</span></a>

  <main class="panel">
    <section class="welcome">
      <h1>WELCOME GUEST!</h1>
      <p>If you can’t find your desired restaurant in the list below simply click the refresh button to show new list of randomized restaurants for you.</p>
    </section>

    <article class="card c1 r1"><div class="photo" role="img" aria-label="Bright dining hall with round white tables" style="background:linear-gradient(#d8c7a6,#8a6a48)"></div><h2>Cool Brown Good Cousine</h2><p>location: 42 elm street, dover NY</p></article>
    <article class="card c2 r1"><div class="photo" role="img" aria-label="Restaurant with blue lit ceiling and glass walls" style="background:linear-gradient(#c9884a,#3d6f8a 60%,#4a3a30)"></div><h2>Blue James Classic Restaurant</h2><p>location: 42 elm street, dover NY</p></article>
    <article class="card c3 r1"><div class="photo" role="img" aria-label="Golden dining room with orange booths" style="background:linear-gradient(#b48a3a,#5a3a1e 55%,#c4552c)"></div><h2>Cirular Restuarant Las Vegas</h2><p>location: 42 elm street, dover NY</p></article>
    <article class="card c4 r1"><div class="photo" role="img" aria-label="Dark elegant dining room with set tables" style="background:linear-gradient(#2a2623,#4a4038 50%,#d8d2c6)"></div><h2>Cirular Restuarant Las Vegas</h2><p>location: 42 elm street, dover NY</p></article>

    <article class="card c1 r2"><div class="photo" role="img" aria-label="Red dining room with hanging lamps" style="background:linear-gradient(#e0a840,#6a2a1c 50%,#d8c8b8)"></div><h2>Cool Brown Good Cousine</h2><p>location: 42 elm street, dover NY</p></article>
    <article class="card c2 r2"><div class="photo" role="img" aria-label="Lounge with blue lights and round sofas" style="background:linear-gradient(#5a4a3e,#2a3a5a 45%,#1e1a1a)"></div><h2>Blue James Classic Restaurant</h2><p>location: 42 elm street, dover NY</p></article>
    <article class="card c3 r2"><div class="photo" role="img" aria-label="Underwater aquarium dining room" style="background:linear-gradient(#5aa8d8,#2a6a9a 60%,#4a5050)"></div><h2>Cirular Restuarant Las Vegas</h2><p>location: 42 elm street, dover NY</p></article>
    <article class="card c4 r2"><div class="photo" role="img" aria-label="Bright arched dining room with white tables" style="background:linear-gradient(#e8c8a0,#c89a70 50%,#7a4a2a)"></div><h2>Cirular Restuarant Las Vegas</h2><p>location: 42 elm street, dover NY</p></article>
  </main>

  <footer class="footer">
    <div class="social"><i></i><i></i><i></i><i></i><i></i></div>
    <div class="rule"></div>
    <nav class="links"><a href="#">HOME</a> &nbsp;·&nbsp; <a href="#">CONTACT US</a></nav>
    <p class="copy">© Copyright 2013 Pickvoro. All Rights Reserved</p>
  </footer>
</div>
</body>
</html>
```